Business Card Design, including supply of raw art files plus a vector diagram of the zelvon logo and

We need the business card design for a company that is launching a new exciting product. The brief requires the submission of the following once the final design is chosen:

- business card layout including raw files
- a composite vector image file of the zelvon logo and tag line
- a standalone vector image file of the zelvon logo

The product will be launched as a customer engagement app.

It has 4 core modules which enables a person to do multiple things - book tours and activities, order takeaways, search for local deals and offers. A universal currency is at the heart of this product. When you use the app, you earn cashback rewards when shopping or buying at any of the merchant partners across the modules as . These rewards can then be used as full or part payment when buying goods or services at these merchant partners.

The business card must help us build the brand, communicate the benefit of the brand's key focus - the ability to earn and burn this universal cashback ccurrency - across the 4 modules - booking of tours and activities, ordering, searching for local deals and payment.

We would like the design to use the brand's blue colour the hex colour is: 00
Dark grey : 646464
Darker blue shadow: 058bdd
Main Blue: 0084ff

We need to translate this into a CMYK print or spot colour print.

Both print options to be supplied as separate files.

An example of the base concept we have in mind is attached for your reference.

The font used by the brand is Proxima Nova.

Note: the duration has been set as 2 days.

Industry/Entity Type

Business

Contact Information for Business Card

Carla Mendoza
Marketing
W: www.zelvon.example
M: + 61 400555123
T: +61 2 5550 1473
A: Suite 7, Level 2, 14-18 Harwick Street, Sydney, NSW, 2000, Australia

Font styles to use
Sans Serif

Requirements
Must have
• zelVon logo and tagline
• address details
• zelVon icons as supplied
Nice to have
• would like to have the option of a spot varnish layer over the logo and icons at the back of the card

```html
<!DOCTYPE html>
<html lang="en">
<head>
<meta charset="utf-8">
<title>zelVon Business Card</title>
<link rel="stylesheet" href="https://fonts.googleapis.com/css2?family=Roboto:wght@300;400&family=Roboto+Condensed:wght@400&display=swap">
<style>
  :root {
    --backdrop: #36393c;
    --brand-blue: #0a8bd2;
    --brand-blue-deep: #0578bd;
    --brand-blue-light: #2a9fe0;
    --dark-grey: #464a4f;
    --mid-grey: #646464;
    --paper: #f7f7f7;
    --white: #ffffff;
  }
  * { margin: 0; padding: 0; box-sizing: border-box; }
  html, body { width: 1200px; height: 576px; overflow: hidden; }
  body {
    background: var(--backdrop);
    font-family: "Roboto", Arial, sans-serif;
    position: relative;
  }
  .card {
    position: absolute;
    top: 138px;
    width: 484px;
    height: 293px;
    overflow: hidden;
  }
  /* Front */
  .card-front {
    left: 81px;
    background: linear-gradient(180deg, var(--brand-blue-light) 0%, var(--brand-blue) 55%, var(--brand-blue-deep) 100%);
    color: var(--white);
  }
  .brand-dot {
    display: block;
    border-radius: 50%;
    background: var(--white);
  }
  .front-dot {
    position: absolute;
    left: 112px;
    top: 62px;
    width: 76px;
    height: 76px;
  }
  .front-name {
    position: absolute;
    left: 201px;
    top: 62px;
    font-weight: 300;
    font-size: 56px;
    line-height: 1;
    letter-spacing: 1px;
    white-space: nowrap;
  }
  .front-tagline {
    position: absolute;
    right: 111px;
    top: 118px;
    font-weight: 300;
    font-size: 16px;
    line-height: 1;
    white-space: nowrap;
  }
  .modules {
    position: absolute;
    left: 0;
    right: 0;
    top: 215px;
    display: flex;
    justify-content: center;
    gap: 10px;
    list-style: none;
  }
  .module {
    width: 76px;
    text-align: center;
    font-family: "Roboto Condensed", Arial, sans-serif;
    font-size: 10px;
    white-space: nowrap;
  }
  .module svg { display: block; margin: 0 auto 6px; width: 32px; height: 32px; }
  /* Back */
  .card-back {
    left: 602px;
    background: var(--paper);
  }
  .person { position: absolute; left: 26px; top: 34px; }
  .person-name { color: var(--brand-blue); font-size: 17px; font-weight: 400; }
  .person-role { color: var(--mid-grey); font-size: 12px; margin-top: 6px; }
  .back-brand {
    position: absolute;
    right: 36px;
    top: 38px;
    display: flex;
    align-items: center;
    gap: 10px;
  }
  .back-brand .brand-dot { width: 56px; height: 56px; background: var(--brand-blue); }
  .back-name {
    color: var(--dark-grey);
    font-weight: 300;
    font-size: 40px;
    line-height: 1;
  }
  .contacts {
    position: absolute;
    left: 28px;
    top: 132px;
    list-style: none;
    color: var(--dark-grey);
    font-size: 12.5px;
    line-height: 16px;
  }
  .contacts li { display: flex; align-items: flex-start; gap: 8px; }
  .contacts svg { width: 10px; height: 10px; margin-top: 3px; flex: none; }
  .waves { position: absolute; left: 0; top: 0; width: 484px; height: 293px; }
  .module-list {
    position: absolute;
    right: 36px;
    top: 208px;
    list-style: none;
    text-align: right;
    color: var(--white);
    font-family: "Roboto Condensed", Arial, sans-serif;
    font-size: 11.5px;
    line-height: 15px;
  }
</style>
</head>
<body>

<section class="card card-front">
  <span class="brand-dot front-dot"></span>
  <span class="front-name">zelVon</span>
  <p class="front-tagline">the cloud currency</p>
  <ul class="modules">
    <li class="module">
      <svg viewBox="0 0 32 32">
        <rect x="3" y="5" width="26" height="22" rx="2" fill="#fff"/>
        <circle cx="17" cy="16" r="7" fill="var(--brand-blue)"/>
        <text x="17" y="20.5" text-anchor="middle" font-size="11" fill="#fff" font-family="Roboto, sans-serif">$</text>
      </svg>
      CashBack Rewards
    </li>
    <li class="module">
      <svg viewBox="0 0 32 32">
        <rect x="2" y="9" width="28" height="19" rx="3" fill="#fff"/>
        <rect x="10" y="5" width="12" height="6" rx="1" fill="#fff"/>
        <circle cx="16" cy="18" r="6" fill="var(--brand-blue)"/>
        <circle cx="16" cy="18" r="4" fill="#fff"/>
      </svg>
      Tours &amp; Activities
    </li>
    <li class="module">
      <svg viewBox="0 0 32 32" stroke="#fff" stroke-width="2.4" stroke-linecap="round" fill="none">
        <path d="M5 4 L26 28"/>
        <path d="M5 4 L5 11 M9 4 L9 11 M5 11 Q7 14 10 12"/>
        <ellipse cx="22" cy="9" rx="4" ry="5.5" fill="#fff" stroke="none"/>
        <path d="M20 13 L6 28"/>
      </svg>
      Mobile Ordering
    </li>
    <li class="module">
      <svg viewBox="0 0 32 32">
        <path d="M14 3 H28 V17 L15 30 L2 17 Z" fill="#fff"/>
        <circle cx="23" cy="8" r="2.4" fill="var(--brand-blue)"/>
      </svg>
      Local Offers
    </li>
  </ul>
</section>

<section class="card card-back">
  <div class="person">
    <h1 class="person-name">Carla Mendoza</h1>
    <p class="person-role">Marketing</p>
  </div>
  <div class="back-brand">
    <span class="brand-dot"></span>
    <span class="back-name">zelVon</span>
  </div>

  <svg class="waves" viewBox="0 0 484 293" aria-hidden="true">
    <path d="M0,268 C120,300 262,250 342,202 C402,166 452,152 484,150 L484,293 L0,293 Z" fill="var(--brand-blue)"/>
    <path d="M0,238 C130,286 270,250 350,196 C405,160 450,149 484,147 L484,156 C442,158 402,176 352,212 C272,266 140,298 0,252 Z" fill="var(--dark-grey)"/>
    <path d="M40,270 C150,292 250,270 330,232 C280,268 160,296 40,274 Z" fill="var(--dark-grey)"/>
  </svg>

  <ul class="contacts">
    <li>
      <svg viewBox="0 0 10 10"><rect x="2" y="0" width="6" height="10" rx="1" fill="var(--brand-blue)"/><rect x="3" y="1.5" width="4" height="6" fill="#fff"/></svg>
      + 61 400555123
    </li>
    <li>
      <svg viewBox="0 0 10 10"><path d="M0 4 Q5 0 10 4 L8 5 L7 3.5 H3 L2 5 Z M2 5.5 H8 V9 H2 Z" fill="var(--brand-blue)"/></svg>
      +61 2 5550 1473
    </li>
    <li>
      <svg viewBox="0 0 10 10" fill="none" stroke="var(--brand-blue)" stroke-width="1"><circle cx="5" cy="5" r="4.3"/><ellipse cx="5" cy="5" rx="1.8" ry="4.3"/><path d="M0.7 5 H9.3"/></svg>
      www.zelvon.example
    </li>
    <li>
      <svg viewBox="0 0 10 10"><path d="M5 10 L1.6 5.2 A4 4 0 1 1 8.4 5.2 Z" fill="var(--brand-blue)"/><circle cx="5" cy="3.6" r="1.5" fill="#fff"/></svg>
      <span>Suite 7, Level 2, 14-18 Harwick Street,<br>Sydney NSW 2000, Australia</span>
    </li>
  </ul>

  <ul class="module-list">
    <li>Local Offers &nbsp;«</li>
    <li>Mobile Ordering &nbsp;«</li>
    <li>Tours &amp; Activities &nbsp;«</li>
    <li>CashBack Rewards &nbsp;«</li>
  </ul>
</section>

</body>
</html>
```